Equestrian business web design and build

I have secured a Brick Loft account and started roughly working through a website, but I need help adding functionality and formatting content. I had Sketch Harbor create a logo for me and now I am at the next step.

Target Market(s)

hunter jumper equestrian community

Industry/Entity Type

equestrian

Coding

Coded - Design and coding required

Font styles to use
Other font styles liked:
• Stranger wide is the font

Requirements
Must have
• Lots of high rez photos, embedded video, charts

```html
<!DOCTYPE html>
<html lang="en">
<head>
<meta charset="utf-8">
<title>Copper Gait</title>
<link href="https://fonts.googleapis.com/css2?family=Michroma&family=Montserrat:wght@400;500;600&display=swap" rel="stylesheet">
<style>
:root{
  --navy:#272a6b;
  --navy-btn:#2b2f7a;
  --steel:#2f5e9e;
  --contact-a:#3a6aab;
  --contact-b:#2f5c98;
  --ink:#1f2130;
  --white:#ffffff;
  --muted:#4a4d5e;
}
*{box-sizing:border-box;margin:0;padding:0}
html,body{width:1200px;height:2294px;overflow:hidden;background:var(--white)}
body{font-family:"Montserrat",sans-serif;color:var(--ink);position:relative}
.display{font-family:"Michroma",sans-serif;letter-spacing:.12em;text-transform:uppercase}

/* Hero */
.hero{position:absolute;left:0;top:0;width:1200px;height:702px;overflow:hidden}
.hero-photo{position:absolute;inset:0;background:
  radial-gradient(ellipse 260px 200px at 600px 300px,#6b4a32 0%,rgba(107,74,50,0) 100%),
  linear-gradient(180deg,#4b5048 0%,#47563f 32%,#5a4e47 55%,#8a7b68 80%,#9b8c76 100%)}
.hero-shade{position:absolute;inset:0;background:linear-gradient(180deg,rgba(20,22,30,.45),rgba(20,22,30,.25) 50%,rgba(20,22,30,.35))}
.brand{position:absolute;left:112px;top:60px;display:flex;align-items:center;gap:10px;color:var(--white);font-size:18px;font-weight:600}
.brand-dot{width:22px;height:22px;border-radius:50%;border:2px solid currentColor}
.nav{position:absolute;top:54px;right:112px;display:flex;align-items:center;font-family:"Michroma",sans-serif;font-size:13px;letter-spacing:.06em;color:var(--white)}
.nav a{color:inherit;text-decoration:none;margin-left:56px}
.nav a:first-child{margin-left:0}
.nav .nav-cta{background:var(--navy-btn);font-family:"Montserrat",sans-serif;font-weight:600;font-size:13px;padding:0 28px;height:42px;line-height:42px;border-radius:3px;margin-left:30px}
.hero-title{position:absolute;left:112px;top:452px;font-size:46px;color:var(--white);letter-spacing:.14em}
.hero-lead{position:absolute;left:115px;top:522px;width:380px;font-size:19px;font-weight:500;line-height:30px;color:var(--white)}
.hero-link{position:absolute;left:115px;top:597px;font-size:16px;color:var(--white);text-decoration:underline}

/* Gallery */
.gallery-title{position:absolute;left:112px;top:782px;font-size:30px;color:var(--ink)}
.tile{position:absolute;top:827px;width:478px;height:366px;display:flex;align-items:center;justify-content:center}
.tile-a{left:111px;background:linear-gradient(160deg,#c9ccc6 0%,#8c6d4d 45%,#c9a93f 85%,#dcc24a 100%)}
.tile-b{left:611px;background:linear-gradient(160deg,#4b6f3a 0%,#38382f 45%,#8a5a38 70%,#cfc4b1 100%)}
.tile-label{color:var(--white);font-size:20px;letter-spacing:.14em}
.gallery-copy{position:absolute;left:112px;top:1208px;width:640px;font-size:20px;line-height:30px;font-weight:500;color:var(--ink)}
.btn{position:absolute;display:block;text-align:center;color:var(--white);font-weight:600;font-size:13px;letter-spacing:.04em;border-radius:3px;text-decoration:none}
.btn-gallery{left:111px;top:1283px;width:147px;height:42px;line-height:42px;background:var(--navy-btn)}

/* About */
.about{position:absolute;left:0;top:1412px;width:1200px;height:366px;background:var(--navy);color:var(--white)}
.about-quote{position:absolute;left:112px;top:94px;width:540px;font-size:21.5px;line-height:32.5px;font-weight:600}
.about-title{position:absolute;left:690px;top:84px;font-size:30px}
.about-text{position:absolute;left:688px;top:136px;width:420px;font-size:15.5px;line-height:25px}
.btn-about{left:688px;top:218px;width:146px;height:42px;line-height:42px;background:var(--steel)}

/* Contact */
.contact{position:absolute;left:0;top:1778px;width:1200px;height:305px;overflow:hidden}
.contact-photo{position:absolute;inset:0;background:radial-gradient(ellipse 500px 220px at 600px 150px,var(--contact-a),var(--contact-b))}
.contact-title{position:absolute;left:0;right:0;top:82px;text-align:center;color:var(--white);font-size:30px;letter-spacing:.16em}
.contact-text{position:absolute;left:0;right:0;top:136px;margin:0 auto;width:420px;text-align:center;color:var(--white);font-size:15.5px;line-height:25px}
.field{position:absolute;top:200px;width:286px;height:42px;background:var(--white);border-radius:2px;font-size:14px;font-weight:500;color:var(--ink);padding-left:19px;line-height:42px}
.field-name{left:84px}.field-phone{left:379px}.field-email{left:675px}
.submit{position:absolute;top:200px;left:970px;width:146px;height:42px;border:1px solid var(--white);border-radius:3px;color:var(--white);font-size:13px;font-weight:600;text-align:center;line-height:40px}

/* Footer */
.footer{position:absolute;left:0;top:2083px;width:1200px;height:211px;font-size:13.5px;color:var(--ink)}
.footer-brand{position:absolute;left:206px;top:80px;display:flex;align-items:center;gap:10px;color:var(--navy);font-size:18px;font-weight:600}
.footer-brand .brand-dot{border-color:var(--navy)}
.footer-address{position:absolute;left:491px;top:56px;line-height:20px}
.footer-phone{position:absolute;left:487px;top:106px}
.footer-links{position:absolute;left:777px;top:54px;list-style:none;line-height:20px}
.footer-social{position:absolute;left:966px;top:64px;width:29px;height:29px;border-radius:50%;border:2.5px solid var(--steel)}
.footer-copy{position:absolute;left:206px;top:170px;font-size:13px;color:var(--muted)}
</style>
</head>
<body>

<header class="hero">
  <div class="hero-photo" role="img" aria-label="Photo of a rider clearing a show-jumping fence in an outdoor arena"></div>
  <div class="hero-shade"></div>
  <div class="brand"><span class="brand-dot"></span>Copper Gait</div>
  <nav class="nav">
    <a href="#">HOME</a>
    <a href="#">ABOUT</a>
    <a href="#">HIGHCREST</a>
    <a href="#">GALLERY</a>
    <a href="#" class="nav-cta">CONTACT US</a>
  </nav>
  <h1 class="hero-title display">Copper Gait</h1>
  <p class="hero-lead">Saers Ikses sepiciatis unde omnis iste natus errorsit voluptatem.</p>
  <a class="hero-link" href="#">Get Started</a>
</header>

<section>
  <h2 class="gallery-title display">Gallery</h2>
  <div class="tile tile-a" role="img" aria-label="Photo of a horse and rider jumping a yellow rail fence"><span class="tile-label display">Errorsit voluptatem</span></div>
  <div class="tile tile-b" role="img" aria-label="Photo of a bay horse and rider in mid-jump against green trees"><span class="tile-label display">Errorsit voluptatem</span></div>
  <p class="gallery-copy">Saers Ikses sepiciatis unde omnis iste natus error sit voluptatem asccusan tium doloremque.</p>
  <a class="btn btn-gallery" href="#">CONTACT US</a>
</section>

<section class="about">
  <p class="about-quote">Daerspiciatis unde omnis iste natus error sit voluptatem accusantium doloremque laudantium, totam rem aperiam, eaque ipsa quae ab illoklkse inventore veritatis et quasi architecto beatae vitae dicta sunt explicabo. Nemo enim ipsam voluptatem quia voluptas sit aspernatur aut odit aut fugit.</p>
  <h2 class="about-title display">About Us</h2>
  <p class="about-text">Saerspiciatis undeasasds aeepoiise osamnis istasesee njhhjkatus error silseoseikst voluptatem accusan tium doloreasmque laudantium.</p>
  <a class="btn btn-about" href="#">LEARN MORE</a>
</section>

<section class="contact">
  <div class="contact-photo" role="img" aria-label="Blue-tinted photo of a show-jumping arena"></div>
  <h2 class="contact-title display">Contact Us</h2>
  <p class="contact-text">Saerspiciatis undeasasds aeepoiise osamnis istasesee njhhjkatus error</p>
  <div class="field field-name">Your Name</div>
  <div class="field field-phone">Phone</div>
  <div class="field field-email">Email</div>
  <div class="submit">SUBMIT</div>
</section>

<footer class="footer">
  <div class="footer-brand"><span class="brand-dot"></span>Copper Gait</div>
  <p class="footer-address">42 Larkspur Rd, Fenwick<br>Ontario, Canada, 10234</p>
  <p class="footer-phone">+1 555 014 2290</p>
  <ul class="footer-links">
    <li>Home</li><li>About</li><li>Highcrest</li><li>Gallery</li><li>Contact Us</li>
  </ul>
  <span class="footer-social" role="img" aria-label="Social profile link"></span>
  <p class="footer-copy">©2023. All rights reserved.</p>
</footer>

</body>
</html>
```